Business Card That Looks Like a Sports Card

Want it to look like a sports trading card. That front should have a baseball player. The back will list our contact info and website info etc.

Contact Information for Business Card

www.ridgecrestathletics.example
visitRCX.example
Email: marcus@ridgecrestathletics.example

Colors

Designer to choose colors to be used in the design.

Requirements
Must have
• Use our current logo and color scheme. Must look like a sports trading card.

```html
<!DOCTYPE html>
<html lang="en">
<head>
<meta charset="utf-8">
<title>Ridgecrest Athletics — Business Card</title>
<link href="https://fonts.googleapis.com/css2?family=Lato:wght@400;700&display=swap" rel="stylesheet">
<style>
  :root {
    --backdrop: #ecebe8;
    --card-navy: #0e1f45;
    --accent-teal: #2ebf9d;
    --text-light: #d5d9e2;
    --text-white: #ffffff;
    --figure-silver: #c3c8d1;
  }
  * { margin: 0; padding: 0; box-sizing: border-box; }
  html, body {
    width: 1200px; height: 847px; overflow: hidden;
    background: var(--backdrop);
    font-family: "Lato", sans-serif;
  }
  .stage {
    position: relative; width: 1200px; height: 847px;
    display: flex; align-items: center; justify-content: center; gap: 40px;
  }
  .card {
    position: relative; width: 540px; height: 309px;
    background: var(--card-navy);
    border-radius: 4px;
    box-shadow: 0 6px 18px rgba(0,0,0,.18);
    overflow: hidden;
  }
  .card-front .batter-artwork {
    position: absolute; left: 110px; top: 30px; width: 190px; height: 255px;
    background:
      radial-gradient(ellipse 42% 48% at 50% 46%,
        rgba(195,200,209,.85) 0%,
        rgba(195,200,209,.55) 40%,
        rgba(195,200,209,.18) 72%,
        rgba(14,31,69,0) 100%);
  }
  .card-back .brand {
    position: absolute; left: 30px; top: 0; width: 230px; height: 100%;
    display: flex; align-items: center; justify-content: center; gap: 10px;
  }
  .brand-dot {
    width: 18px; height: 18px; border-radius: 50%; background: var(--accent-teal); flex: none;
  }
  .brand-name {
    color: var(--text-white); font-weight: 700; font-size: 22px; line-height: 1.15;
    text-transform: uppercase; letter-spacing: .5px;
  }
  .card-back .divider {
    position: absolute; left: 280px; top: 70px; width: 1px; height: 170px;
    background: var(--accent-teal); opacity: .7;
  }
  .card-back .contact {
    position: absolute; left: 300px; top: 92px; right: 14px;
    color: var(--text-light); font-size: 12.5px; line-height: 1.45;
  }
  .contact-name { color: var(--accent-teal); font-weight: 700; font-size: 19px; line-height: 1.1; }
  .contact-title { margin-bottom: 12px; }
  .contact-address { margin-bottom: 6px; }
  .contact-row { display: flex; align-items: center; gap: 7px; white-space: nowrap; }
  .contact-row svg { width: 11px; height: 11px; flex: none; }
  .site-highlight { color: var(--accent-teal); }
</style>
</head>
<body>
<main class="stage">
  <section class="card card-front">
    <div class="batter-artwork" role="img" aria-label="Silver silhouette illustration of a baseball batter mid-swing"></div>
  </section>

  <section class="card card-back">
    <div class="brand">
      <span class="brand-dot"></span>
      <span class="brand-name">Ridgecrest<br>Athletics</span>
    </div>
    <div class="divider"></div>
    <div class="contact">
      <p class="contact-name">Daniel Reyes</p>
      <p class="contact-title">Founder &amp; CEO</p>
      <p class="contact-address">4410 Meadowlark Lane, Suite 300,<br>Ridgecrest, Ohio 45210</p>
      <p class="contact-row">
        <svg viewBox="0 0 12 12"><path d="M2.5 1h2l1 2.5-1.3 1a6 6 0 0 0 3.3 3.3l1-1.3L11 7.5v2c0 .8-.7 1.5-1.5 1.5A8.5 8.5 0 0 1 1 2.5C1 1.7 1.7 1 2.5 1z" fill="var(--accent-teal)"/></svg>
        +100 555 0142
      </p>
      <p class="contact-row">
        <svg viewBox="0 0 12 12"><rect x="0.5" y="2" width="11" height="8" rx="1" fill="var(--accent-teal)"/><path d="M1 2.5l5 4 5-4" stroke="var(--card-navy)" fill="none"/></svg>
        marcus@ridgecrestathletics.example
      </p>
      <p class="contact-row">
        <svg viewBox="0 0 12 12"><circle cx="6" cy="6" r="5" fill="none" stroke="var(--accent-teal)" stroke-width="1.3"/><path d="M1 6h10M6 1c2 2.5 2 7.5 0 10M6 1c-2 2.5-2 7.5 0 10" stroke="var(--accent-teal)" fill="none" stroke-width=".9"/></svg>
        <span>www.<span class="site-highlight">ridgecrestathletics</span>.example</span>
      </p>
    </div>
  </section>
</main>
</body>
</html>
```